Design and develop an e-commerce website for Our Hearthline Appliances store

Design and develop an e-commerce website for Our Hearthline Appliances store that sells Hearthline Appliances such as pots, kettle, plates, dish washer, microwave,
gas cooker, heat extractor etc.
I want any good shopping cart platform such as Bigcommerce, Wordpress, Bigcartel, Woocommerce and others .We want a new template. No need to install it on our website, we will take care of that.

To win the contest please present a sample of:
- the home page
- the product page
- the page where all the items that we sale are listed
- the shopping cart page

I have written some information here for you.

PLEASE READ DESCRIPTION CAREFULLY.

The website i require will have a several areas. Products, which prices that can be added to shopping basket.
I also require the site to have a customer login facility , so that once a customer has used the site they
can login themselves at a later stage and see previous orders and then repeat an order if required.

Must have

Logo must be included.
I would also need to able to manage this site myself, by adding new items and deleting items that are no longer available.

Good luck and for any question please don't hesitate to ask

```html
<!DOCTYPE html>
<html lang="en">
<head>
<meta charset="utf-8">
<title>Hearthline Appliances — Home</title>
<link href="https://fonts.googleapis.com/css2?family=Lato:wght@300;400;700;900&display=swap" rel="stylesheet">
<style>
:root{
  --accent:#f5b82e;
  --ink:#1a1a1a;
  --nav:#2a2a2a;
  --nav-deep:#1a1a1a;
  --muted:#777;
  --line:#dcdcdc;
  --cream:#f3efe6;
  --footer:#1e1e1e;
  --white:#fff;
}
*{box-sizing:border-box;margin:0;padding:0}
html,body{width:1200px;height:3061px;overflow:hidden}
body{position:relative;font-family:'Lato',sans-serif;color:var(--ink);background:var(--white)}
.abs{position:absolute}
svg{display:block}

/* top bar */
.topbar{top:0;left:0;width:1200px;height:41px;background:var(--white);font-size:15px;font-weight:700}
.topbar .greet{left:32px;top:11px}
.topbar .greet span{color:var(--accent)}
.topbar .social{left:512px;top:9px;display:flex;gap:14px}
.topbar .social i{width:20px;height:20px;border-radius:50%;background:#333;display:block}
.topbar .prefs{right:10px;top:10px;display:flex;gap:30px;font-size:16px}
.topbar .prefs span{display:flex;align-items:center;gap:6px}

/* nav */
.nav{top:41px;left:0;width:1200px;height:106px;background:var(--nav);color:var(--white);font-weight:700;font-size:19px}
.nav .item{top:39px;display:flex;align-items:center;gap:12px}
.brandbox{left:461px;top:0;width:267px;height:106px;background:var(--nav-deep);display:flex;align-items:center;justify-content:center;gap:10px}
.brandbox .mark{width:14px;height:14px;background:var(--accent)}
.brandbox .name{color:var(--accent);font-size:30px;font-weight:900;letter-spacing:1px}

/* hero */
.hero{top:147px;left:0;width:1200px;height:553px;background:linear-gradient(180deg,#9c9b98 0%,#c6c5c1 22%,#d2d1cd 60%,#bab9b4 100%)}
.hero .product{left:740px;top:120px;width:430px;height:433px;background:linear-gradient(180deg,rgba(60,60,60,.0) 0%,#6e6a66 18%,#8a2f2a 55%,#7c6a34 78%,#9a8e6a 100%);opacity:.85}
.hero .kicker{left:146px;top:205px;color:var(--accent);font-size:27px;font-weight:900}
.hero h1{left:141px;top:238px;color:var(--white);font-size:48px;font-weight:900;text-shadow:0 2px 4px rgba(0,0,0,.35)}
.hero .sub{left:145px;top:298px;color:var(--white);font-size:31px;font-weight:700;text-shadow:0 2px 4px rgba(0,0,0,.35)}
.hero .cta{left:147px;top:363px;width:214px;height:57px;border:3px solid var(--white);color:var(--white);font-weight:700;font-size:20px;display:flex;align-items:center;justify-content:center;background:rgba(0,0,0,.25)}
.hero .pager{top:186px;width:39px;height:137px;border:2px solid var(--white);color:var(--white);font-weight:900;font-size:19px;display:flex;flex-direction:column;align-items:center;justify-content:center;line-height:1.25}

/* features */
.features{top:700px;left:0;width:1200px;height:102px;background:var(--cream)}
.features .feat{top:38px;display:flex;align-items:center;gap:10px;font-weight:700;font-size:19px;color:#555}

/* promo grid */
.promo{top:845px;left:161px;width:876px;height:502px}
.promo .tile{position:absolute}
.tile-future{left:0;top:0;width:586px;height:273px;background:linear-gradient(180deg,#dcdcdc 0%,#e6e4e1 45%,#d8cfc6 70%,#a9a6a2 100%)}
.tile-new{left:586px;top:0;width:290px;height:273px;background:linear-gradient(180deg,#f4f4f4 0%,#e4e4e4 55%,#d9d9d9 100%)}
.tile-hot{left:0;top:273px;width:876px;height:229px;background:linear-gradient(180deg,#2a2a28 0%,#3d3934 40%,#23221f 100%)}
.tile-future .title{left:66px;top:33px;color:var(--white);font-size:27px;font-weight:900}
.btn-outline{border:2px solid var(--white);color:var(--white);font-weight:700;display:flex;align-items:center;justify-content:center}
.tile-future .btn-outline{left:66px;top:73px;width:142px;height:37px;font-size:17px}
.tile-new .caption{left:0;top:180px;width:290px;text-align:center}
.tile-new .caption .l1{color:var(--muted);font-size:20px}
.tile-new .caption .l2{font-size:27px;font-weight:900;margin-top:6px}
.hot-box{left:96px;top:41px;width:682px;height:147px;border:3px solid var(--white);background:rgba(0,0,0,.55)}
.hot-tag{left:368px;top:25px;width:138px;height:31px;background:var(--accent);color:var(--white);font-weight:900;font-size:15px;display:flex;align-items:center;justify-content:center}
.hot-box p{left:20px;top:38px;width:636px;color:var(--white);font-size:14px;text-align:center;line-height:1.7}
.hot-box .btn-outline{left:266px;top:95px;width:146px;height:39px;font-size:16px;background:#111}

/* collection */
.collection{top:1420px;left:0;width:1200px;height:403px;background:linear-gradient(180deg,#1a1a1a,#262626 60%,#1c1c1c)}
.collection .fridge{left:820px;top:60px;width:300px;height:343px;background:linear-gradient(180deg,#2e2e2e,#3a3a3a 50%,#2a2a2a)}
.collection .centre{left:0;width:1200px;text-align:center;color:var(--white)}
.collection .c1{top:78px;font-size:23px;font-weight:700}
.collection .c2{top:110px;font-size:48px;font-weight:900}
.collection .c3{top:204px;font-size:18px;font-weight:700}
.collection .btn-outline{left:492px;top:262px;width:188px;height:57px;font-size:20px;border-width:3px}

/* best seller */
.best h2{left:0;top:1862px;width:1200px;text-align:center;font-size:40px;font-weight:900}
.best .rule{left:527px;top:1914px;width:146px;height:3px;background:var(--ink)}
.best .sub{left:0;top:1929px;width:1200px;text-align:center;font-size:18px;color:#666}
.filters{left:145px;top:1982px;display:flex;gap:30px;font-size:21.5px;color:#777;font-weight:700}
.filters .on{color:var(--accent)}
.grid-line{background:var(--line)}
.cell{position:absolute;width:284px;height:215px}
.cell .photo{position:absolute;left:50px;top:16px;width:160px;height:128px}
.cell .name{position:absolute;left:30px;top:152px;font-size:20px;color:#555}
.cell .price{position:absolute;right:20px;top:176px;font-size:22px;font-weight:900;color:var(--accent)}
.cell .icons{position:absolute;right:14px;top:16px}
.show-more{left:500px;top:2480px;width:190px;height:57px;border:3px solid var(--ink);font-weight:900;font-size:20px;display:flex;align-items:center;justify-content:center}

/* partners */
.partner{top:2600px;display:flex;align-items:center;gap:14px}
.partner .dot{width:56px;height:56px;border-radius:50%;background:#d9d9d9}
.partner .txt{line-height:1;color:#444}
.partner .txt b{display:block;font-size:37px;font-weight:700}
.partner .txt span{font-size:30px;font-weight:300}

/* footer */
.footer{top:2721px;left:0;width:1200px;height:290px;background:var(--footer);color:var(--white)}
.footer .sep{top:0;width:3px;height:290px;background:#555}
.footer .col{top:0;text-align:center}
.footer h3{margin-top:67px;font-size:21px;font-weight:700}
.footer .info{font-size:15px;line-height:31px;margin-top:28px;color:#ddd}
.footer .info div{display:flex;align-items:center;gap:12px;justify-content:flex-end}
.footer .connect{font-size:14px;color:#ddd;margin-top:34px}
.footer .icons{display:flex;gap:26px;justify-content:center;margin-top:22px}
.footer .icons i{width:30px;height:30px;border-radius:50%;background:#e5e5e5;display:block}
.sub-field{left:835px;top:161px;width:278px;height:54px;border:2px solid #888;font-size:15px;color:#bbb;padding:16px 18px}
.sub-btn{left:1113px;top:161px;width:65px;height:54px;background:var(--accent);display:flex;align-items:center;justify-content:center}
.copyright{top:3011px;left:0;width:1200px;height:50px;text-align:center;padding-top:15px;font-size:19px;color:#444}
.copyright span{color:var(--accent)}
</style>
</head>
<body>

<header class="topbar abs">
  <div class="greet abs">Hi, wellcome to <span>Hearthline Appliances</span> stores!</div>
  <div class="social abs" aria-label="Social links"><i></i><i></i><i></i><i></i><i></i></div>
  <div class="prefs abs">
    <span>Language: English <svg width="14" height="9"><path d="M0 0h14L7 9z" fill="#1a1a1a"/></svg></span>
    <span>Currency: USD <svg width="14" height="9"><path d="M0 0h14L7 9z" fill="#1a1a1a"/></svg></span>
  </div>
</header>

<nav class="nav abs">
  <div class="item abs" style="left:66px">
    <svg width="30" height="22"><rect y="0" width="30" height="4" fill="#fff"/><rect y="9" width="30" height="4" fill="#fff"/><rect y="18" width="30" height="4" fill="#fff"/></svg>MENU
  </div>
  <div class="item abs" style="left:264px">
    <svg width="24" height="24"><circle cx="10" cy="10" r="7.5" stroke="#fff" stroke-width="3" fill="none"/><line x1="15.5" y1="15.5" x2="22" y2="22" stroke="#fff" stroke-width="3"/></svg>SEARCH
  </div>
  <div class="brandbox abs"><span class="mark"></span><span class="name">HEARTHLINE</span></div>
  <div class="item abs" style="left:792px">
    <svg width="22" height="24"><circle cx="11" cy="7" r="6" fill="#fff"/><path d="M0 24c0-7 5-10 11-10s11 3 11 10z" fill="#fff"/></svg>MY ACCOUNT
  </div>
  <div class="item abs" style="left:1010px">
    <svg width="30" height="24"><path d="M1 3h5l4 14h15l3-10H8" stroke="#fff" stroke-width="2.5" fill="none"/><circle cx="12" cy="21" r="2" fill="#fff"/><circle cx="23" cy="21" r="2" fill="#fff"/></svg>CART (0)
  </div>
</nav>

<section class="hero abs" role="img" aria-label="Kitchen scene: white brick wall, three black pendant lamps and a red blender surrounded by fresh fruit and vegetables">
  <div class="product abs"></div>
  <div class="pager abs" style="left:67px">P<br>R<br>E<br>V</div>
  <div class="pager abs" style="left:1075px">N<br>E<br>X<br>T</div>
  <div class="kicker abs">BEST PRODUCT</div>
  <h1 class="abs">KITCHEN APPLIANCES</h1>
  <div class="sub abs">Last chance to Buy extra 60% off</div>
  <div class="cta abs">VIEW COLLECTION</div>
</section>

<section class="features abs">
  <div class="feat abs" style="left:114px">
    <svg width="38" height="26"><rect x="1" y="3" width="22" height="16" fill="#555"/><path d="M23 8h8l6 6v5H23z" fill="#555"/><circle cx="8" cy="21" r="4" fill="#555" stroke="#f3efe6" stroke-width="2"/><circle cx="30" cy="21" r="4" fill="#555" stroke="#f3efe6" stroke-width="2"/></svg>FREE SHIPPING
  </div>
  <div class="feat abs" style="left:373px">
    <svg width="26" height="26"><path d="M2 2h11l11 11-11 11L2 13z" fill="#555"/><circle cx="8" cy="8" r="2.5" fill="#f3efe6"/></svg>WEEKLY DISCOUNT
  </div>
  <div class="feat abs" style="left:661px">
    <svg width="28" height="28"><circle cx="14" cy="14" r="12" stroke="#555" stroke-width="3" fill="none"/><path d="M14 6a8 8 0 1 0 8 8h-8z" fill="#555"/></svg>FREE RETURN
  </div>
  <div class="feat abs" style="left:900px">
    <svg width="24" height="28"><path d="M5 2l5 1 1 7-4 2c2 5 4 8 8 10l2-4 7 2-1 6c-12 0-22-10-22-22z" fill="#555"/></svg>SUPPORT 24/7
  </div>
</section>

<section class="promo abs">
  <div class="tile tile-future" role="img" aria-label="Stack of white and blush ceramic bowls on a kitchen counter">
    <div class="title abs">FUTURE PRODUCTS</div>
    <div class="btn-outline abs">BUY NOW</div>
  </div>
  <div class="tile tile-new" role="img" aria-label="Stainless steel whistling kettle with a wooden handle">
    <div class="caption abs"><div class="l1">LOREM IPSUM</div><div class="l2">NEW IN 2016</div></div>
  </div>
  <div class="tile tile-hot" role="img" aria-label="Pan of pasta on a black induction cooktop beside fresh vegetables">
    <div class="hot-box abs">
      <p class="abs">Lorem ipsum dolor sit amet, consectetuer adipiscing elit, sed diam nonummy nibh euismod tincid-<br>unt ut laoreet dolore magna aliquam erat</p>
      <div class="btn-outline abs">BUY NOW</div>
    </div>
    <div class="hot-tag abs">HOT SALE</div>
  </div>
</section>

<section class="collection abs" role="img" aria-label="Dark kitchen with a black double-door refrigerator and a range cooker">
  <div class="fridge abs"></div>
  <div class="centre c1 abs">ACCESORIES</div>
  <div class="centre c2 abs">NEW COLLECTION</div>
  <div class="centre c3 abs">Mazim placerat facer possim assum typinon habent claritatem legentis in quifacit eorum claritatem</div>
  <div class="btn-outline abs">EXPLORE NOW</div>
</section>

<section class="best">
  <h2 class="abs">BEST SELLER</h2>
  <div class="rule abs"></div>
  <div class="sub abs">Best Seller Produts</div>
  <div class="filters abs">
    <span class="on">ALL</span><span>Pots</span><span>Gas Cooker</span><span>Dish Washer</span><span>Plates</span><span>Kettle</span><span>Microwave</span><span>Heat Extractor</span>
  </div>

  <div class="grid-line abs" style="left:0;top:2036px;width:1200px;height:3px"></div>
  <div class="grid-line abs" style="left:0;top:2254px;width:1200px;height:3px"></div>
  <div class="grid-line abs" style="left:0;top:2458px;width:1200px;height:3px"></div>
  <div class="grid-line abs" style="left:153px;top:2036px;width:3px;height:425px"></div>
  <div class="grid-line abs" style="left:439px;top:2036px;width:3px;height:425px"></div>
  <div class="grid-line abs" style="left:739px;top:2036px;width:3px;height:425px"></div>
  <div class="grid-line abs" style="left:1024px;top:2036px;width:3px;height:425px"></div>

  <div class="cell" style="left:156px;top:2039px">
    <div class="photo" role="img" aria-label="White and orange electric lunch box" style="background:radial-gradient(ellipse 60% 45% at 50% 55%,#f08a3c 0%,#f4c9a6 55%,#fff 100%)"></div>
    <div class="icons"><svg width="18" height="36"><path d="M9 15 2 8a3.5 3.5 0 0 1 7-3 3.5 3.5 0 0 1 7 3z" fill="none" stroke="#f5b82e" stroke-width="1.5"/><ellipse cx="9" cy="28" rx="7" ry="4" fill="none" stroke="#f5b82e" stroke-width="1.5"/><circle cx="9" cy="28" r="2" fill="#f5b82e"/></svg></div>
    <div class="name">Lorem Ipsum</div><div class="price">$99</div>
  </div>
  <div class="cell" style="left:442px;top:2039px">
    <div class="photo" role="img" aria-label="Red electric kettle" style="background:radial-gradient(ellipse 40% 48% at 50% 55%,#b8141c 0%,#e3a0a3 60%,#fff 100%)"></div>
    <div class="icons"><svg width="18" height="36"><path d="M9 15 2 8a3.5 3.5 0 0 1 7-3 3.5 3.5 0 0 1 7 3z" fill="none" stroke="#f5b82e" stroke-width="1.5"/><ellipse cx="9" cy="28" rx="7" ry="4" fill="none" stroke="#f5b82e" stroke-width="1.5"/><circle cx="9" cy="28" r="2" fill="#f5b82e"/></svg></div>
    <div class="name">Lorem Ipsum</div><div class="price">$99</div>
  </div>
  <div class="cell" style="left:742px;top:2039px">
    <div class="photo" role="img" aria-label="Set of orange mixing bowls" style="background:radial-gradient(ellipse 48% 38% at 50% 55%,#e8661c 0%,#f4b48a 60%,#fff 100%)"></div>
    <div class="icons"><svg width="18" height="36"><path d="M9 15 2 8a3.5 3.5 0 0 1 7-3 3.5 3.5 0 0 1 7 3z" fill="none" stroke="#f5b82e" stroke-width="1.5"/><ellipse cx="9" cy="28" rx="7" ry="4" fill="none" stroke="#f5b82e" stroke-width="1.5"/><circle cx="9" cy="28" r="2" fill="#f5b82e"/></svg></div>
    <div class="name">Lorem Ipsum</div><div class="price">$99</div>
  </div>
  <div class="cell" style="left:156px;top:2257px">
    <div class="photo" role="img" aria-label="Stainless steel dishwasher" style="background:radial-gradient(ellipse 32% 48% at 50% 50%,#8f8f8f 0%,#cfcfcf 60%,#fff 100%)"></div>
    <div class="icons"><svg width="18" height="36"><path d="M9 15 2 8a3.5 3.5 0 0 1 7-3 3.5 3.5 0 0 1 7 3z" fill="none" stroke="#f5b82e" stroke-width="1.5"/><ellipse cx="9" cy="28" rx="7" ry="4" fill="none" stroke="#f5b82e" stroke-width="1.5"/><circle cx="9" cy="28" r="2" fill="#f5b82e"/></svg></div>
    <div class="name">Lorem Ipsum</div><div class="price">$99</div>
  </div>
  <div class="cell" style="left:442px;top:2257px">
    <div class="photo" role="img" aria-label="Silver and black microwave oven" style="background:radial-gradient(ellipse 45% 42% at 50% 50%,#3a3a3a 0%,#b5b5b5 60%,#fff 100%)"></div>
    <div class="icons"><svg width="18" height="36"><path d="M9 15 2 8a3.5 3.5 0 0 1 7-3 3.5 3.5 0 0 1 7 3z" fill="none" stroke="#f5b82e" stroke-width="1.5"/><ellipse cx="9" cy="28" rx="7" ry="4" fill="none" stroke="#f5b82e" stroke-width="1.5"/><circle cx="9" cy="28" r="2" fill="#f5b82e"/></svg></div>
    <div class="name">Lorem Ipsum</div><div class="price">$99</div>
  </div>
  <div class="cell" style="left:742px;top:2257px">
    <div class="photo" role="img" aria-label="Black single induction hob" style="background:radial-gradient(ellipse 45% 35% at 50% 50%,#1e1e1e 0%,#a8a8a8 60%,#fff 100%)"></div>
    <div class="icons"><svg width="18" height="36"><path d="M9 15 2 8a3.5 3.5 0 0 1 7-3 3.5 3.5 0 0 1 7 3z" fill="none" stroke="#f5b82e" stroke-width="1.5"/><ellipse cx="9" cy="28" rx="7" ry="4" fill="none" stroke="#f5b82e" stroke-width="1.5"/><circle cx="9" cy="28" r="2" fill="#f5b82e"/></svg></div>
    <div class="name">Lorem Ipsum</div><div class="price">$99</div>
  </div>

  <div class="show-more abs">SHOW MORE</div>
</section>

<section class="partners">
  <div class="partner abs" style="left:112px"><span class="dot"></span><div class="txt"><span>LOGO</span><b>BRAND</b></div></div>
  <div class="partner abs" style="left:378px"><span class="dot"></span><div class="txt"><span>LOGO</span><b>BRAND</b></div></div>
  <div class="partner abs" style="left:633px"><span class="dot"></span><div class="txt"><span>LOGO</span><b>BRAND</b></div></div>
  <div class="partner abs" style="left:870px"><span class="dot"></span><div class="txt"><span>LOGO</span><b>BRAND</b></div></div>
</section>

<footer class="footer abs">
  <div class="sep abs" style="left:387px"></div>
  <div class="sep abs" style="left:809px"></div>
  <div class="col abs" style="left:0;width:387px">
    <h3>CONTACT US</h3>
    <div class="info" style="padding-right:26px">
      <div><svg width="18" height="16"><path d="M9 1 1 8h2v7h4v-4h4v4h4V8h2z" fill="#ccc"/></svg>No. 48 Maple Row, Cedar St, Springfield</div>
      <div style="padding-right:40px"><svg width="16" height="18"><path d="M3 1l4 1 1 5-3 1c1 3 3 5 6 7l2-3 4 2-1 4C7 18 0 11 0 2z" fill="#ccc"/></svg>(+100) 5550 123 4567</div>
      <div style="padding-right:28px"><svg width="20" height="14"><rect width="20" height="14" fill="#ccc"/><path d="M0 0l10 8 10-8" stroke="#1e1e1e" stroke-width="1.5" fill="none"/></svg>hello@hearthline.example</div>
    </div>
  </div>
  <div class="col abs" style="left:390px;width:419px">
    <h3>CONNECT WITH US</h3>
    <div class="connect">Join the conversation about modern design</div>
    <div class="icons" aria-label="Social links"><i></i><i></i><i></i><i></i></div>
  </div>
  <div class="col abs" style="left:812px;width:388px">
    <h3>NEWSLETTER</h3>
    <div class="connect">Claritas processus dynamicus sequitu consution</div>
  </div>
  <div class="sub-field abs">Your e-mail adress</div>
  <div class="sub-btn abs"><svg width="30" height="24"><path d="M2 12h24M16 3l10 9-10 9" stroke="#fff" stroke-width="4" fill="none"/></svg></div>
</footer>

<div class="copyright abs">© 2016 <span>Hearthline Appliances</span>- All rights reserved.</div>

</body>
</html>
```